Events and Parties web-site needs a Web Design

VoTrel needs a web design.
VoTrel means The Bees in Italian.
VoTrel target market is people who is organizing parties and events.
Our mission is that the parties and events of our clients exceed their expectations by providing them web and mobile tools.
Our vision is to be the best and biggest party web portal of the country.
The main features of our web site is to let people invite guests and search suppliers/providers. Guests will also confirm presence (RSVP) and buy presents/gifts at the site as well.
Our slogan is "Curta sua festa desde já !" that means "Enjoy our party now !" in Brazilian Portuguese.
The idea here is that the party starts now and not only at the scheduled date and time.
Updates
It seems that must have and nice to have briefing is not appearing to you as I filled. So I will type it agai here:
Our slogan text that is "Curta sua festa desde já !" that means "Enjoy your party now !".
Space to paid ads.
Language switch to Spanish. Brazilian Portuguese is our default language.
Logon form with 2 inputs: Email and password.
RSVP form with 2 inputs: Event ID and password
Kendro trusted site seal (SSL/HTTPS) logo.
Update to my briefing: Only event organizer and guests will be able to see details of the events/parties like photos/blog, guest list and etc. Suppliers will be searched and rated like stayvoro.com/roamgliq.
Target Market(s)
VoTrel target market is amateur and professional people who are organizing parties and events.
Our mission is that the parties and events of our clients exceed their expectations by providing them easy and fast web and mobile tools.
Our vision is to be the best and biggest party portal of our country.
The main features of our web site is to let people invite guests and search suppliers/providers. Guests will also confirm presence (RSVP) and buy presents at the site.
Industry/Entity Type
Events
Requirements
Must have
- Design and colors compliant with attached logo.
- Our slogan text that is "Curta sua festa desde já !" that means "Enjoy your party now !".
- Space to paid ads.
- Language switch to Spanish. Brazilian Portuguese is our default language.
- Logon form with 2 inputs: Email and password.
- RSVP form with 2 inputs: Event ID and password
- Kendro trusted site seal (SSL/HTTPS) logo.
Nice to have
- VoTrel stands for The Bees in Italian. It would be very nice to have a not so explicit idea that each user is a bee and VoTrel is the hive where party/event occurs.
Should not have
- No PageMill please.
- No infant/child oriented designs please. Our market is not only children birthdays but also other parties and events like marriages, corporate events and so on

```html
<!DOCTYPE html>
<html lang="pt-BR">
<head>
<meta charset="utf-8">
<title>VoTrel – Curta sua festa desde já</title>
<link rel="stylesheet" href="https://fonts.googleapis.com/css2?family=Open+Sans:wght@400;600;700&family=Merriweather:wght@400;700&display=swap">
<style>
:root{
  --honey:#f5b30c;
  --honey-deep:#e0a10a;
  --honey-dark:#d4950a;
  --honey-mid:#eaab10;
  --honey-soft:#f7c35a;
  --footer:#b07c02;
  --cocoa:#2e0a05;
  --mauve:#6e5a5a;
  --title:#6e4a4a;
  --text:#444;
  --muted:#999;
  --line:#e4e4e4;
  --mist:#f2f2f2;
  --white:#fff;
}
*{box-sizing:border-box;margin:0;padding:0}
html,body{width:855px;height:1200px;overflow:hidden}
body{position:relative;background:var(--white);font-family:"Open Sans",Arial,sans-serif;color:var(--text);font-size:8px}
.abs{position:absolute}

.hero-band{left:0;top:0;width:855px;height:427px;background:var(--mist)}
.topbar{left:160px;top:0;width:535px;height:17px;background:var(--honey);color:var(--white);font-size:7px;font-weight:600;display:flex;align-items:center;justify-content:space-between;padding:0 16px}
.topbar .links span{margin-right:6px}
.topbar .contact{display:flex;gap:12px;align-items:center}
.topbar .contact svg{vertical-align:-1px;margin-right:3px}
.header{left:160px;top:17px;width:535px;height:56px;background:var(--white)}
.brand{left:6px;top:20px;display:flex;align-items:center;gap:5px;font-family:"Open Sans",Arial,sans-serif;font-size:17px;color:var(--honey-dark)}
.brand i{display:block;width:14px;height:14px;border-radius:50%;background:var(--cocoa)}
.social{right:26px;top:19px;display:flex;gap:3px}
.social span{width:16px;height:16px;border-radius:50%;background:#8a8a8a}
.nav{left:160px;top:73px;width:535px;height:28px;background:var(--white);border-top:1px solid var(--line);border-bottom:1px solid var(--line);display:flex;font-size:8px;font-weight:600;color:#333}
.nav a{display:flex;align-items:center;justify-content:center;border-right:1px solid var(--line);text-decoration:none;color:inherit;gap:4px}
.nav a.active{border-bottom:2px solid var(--honey)}
.nav .search{margin-left:auto;width:41px;border-left:1px solid var(--line);border-right:0}

.slide-arrow{top:206px;width:32px;height:64px;background:var(--white);display:flex;align-items:center;justify-content:center}
.slide-arrow.left{left:0;border-right:2px solid var(--cocoa)}
.slide-arrow.right{right:0;border-left:2px solid var(--cocoa)}
.slogan{left:160px;height:31px;color:var(--white);font-family:"Merriweather",Georgia,serif;font-size:16px;font-weight:400;display:flex;align-items:center;padding:0 8px;white-space:nowrap;width:auto}
.slogan.pt{top:206px;background:var(--honey-soft)}
.slogan.en{top:238px;background:var(--mauve)}
.hero-photo{left:370px;top:150px;width:325px;height:226px;background:radial-gradient(ellipse at 65% 45%,#b89a86 0%,#d9cdc6 45%,var(--mist) 75%)}

.features{left:160px;top:376px;width:535px;height:102px;display:flex}
.feature{width:107px;display:flex;flex-direction:column;align-items:center;padding-top:22px;color:var(--white);font-family:"Merriweather",Georgia,serif;font-size:10px;font-weight:700}
.feature .badge{width:40px;height:40px;border-radius:50%;background:var(--white);display:flex;align-items:center;justify-content:center;margin-bottom:11px}
.f1{background:var(--honey-deep)}.f2{background:var(--honey-dark)}.f3{background:var(--honey-mid)}.f4{background:var(--honey)}.f5{background:var(--cocoa)}

.content{left:160px;top:478px;width:535px;height:500px;border-left:1px solid var(--line);border-right:1px solid var(--line)}
.col-rule{top:0;height:500px;width:1px;background:var(--line)}
.hrule{height:1px;background:var(--line)}
.block-title{height:18px;background:var(--honey);color:var(--cocoa);font-family:"Merriweather",Georgia,serif;font-size:8px;font-weight:700;display:flex;align-items:center;justify-content:space-between;padding:0 6px}
.block-title.dark{background:var(--cocoa);color:var(--white)}
.pager{display:flex;gap:3px}
.pager span{width:10px;height:10px;border-radius:50%;background:var(--white);display:flex;align-items:center;justify-content:center}
.copy{font-size:7.5px;line-height:13px;color:var(--text)}
.field{height:19px;border:1px solid var(--line);font-size:6px;color:#bbb;padding:0 6px;display:flex;align-items:center;justify-content:space-between}
.btn{height:19px;border:1px solid var(--line);background:#fafafa;font-size:6.5px;font-weight:700;color:#333;display:flex;align-items:center;justify-content:center}
.seal{width:30px;height:24px;background:#dfe4ee;border:1px solid #b9c0cf;border-radius:2px}

.news-item .thumb{width:36px;height:36px;border-radius:50%;background:var(--mist);flex:none}
.news-item h4{font-size:7.8px;font-weight:600;color:var(--title);white-space:nowrap}
.news-item .date{font-size:6.5px;color:var(--muted);margin:1px 0 4px}
.video{background:var(--mist)}
.ad{width:83px;height:26px;background:var(--mist)}
.event .cal{width:27px;height:30px;border:1px solid var(--line);text-align:center}
.event .cal b{display:block;background:var(--mauve);color:var(--white);font-size:6.5px;height:10px;line-height:10px}
.event .cal span{font-size:12px;color:#333;line-height:19px}
.event h4{font-size:7.8px;font-weight:600;color:var(--honey);line-height:10.5px}
.event p{font-size:6.5px;color:var(--muted);margin-top:2px}

.footer{left:0;top:978px;width:855px;height:222px;background:var(--footer);color:var(--white)}
.foot-title{font-family:"Merriweather",Georgia,serif;font-size:8.5px;font-weight:700;position:absolute;top:37px}
.foot-title::after{content:"";display:block;width:23px;height:2px;background:var(--cocoa);margin-top:5px}
.foot-copy{font-size:7.4px;line-height:13px}
.tags{display:flex;flex-wrap:wrap;gap:6px 5px;width:110px}
.tags span{background:var(--cocoa);color:var(--white);font-size:7.5px;padding:0 6px;height:17px;display:flex;align-items:center}
.tweet{font-size:7.3px;line-height:12.5px;font-style:italic}
.tweet b{color:var(--cocoa);font-weight:400}
.tweet small{display:block;font-style:normal;font-size:6.5px;opacity:.85;margin-top:1px}
.gallery{display:grid;grid-template-columns:repeat(3,35px);gap:5px}
.gallery span{height:35px;background:#f2f2f2}
.bottom-bar{left:177px;top:194px;width:502px;height:28px;background:var(--honey);display:flex;align-items:center;justify-content:space-between;padding:0 10px;font-size:7px;color:var(--cocoa)}
</style>
</head>
<body>

<div class="abs hero-band"></div>

<div class="abs topbar">
  <div class="links"><span>Link</span><span>Link</span><span>Link</span><span>Link</span><span>Link</span></div>
  <div class="contact">
    <span><svg width="7" height="7" viewBox="0 0 10 10"><path d="M2 0l2 2-1 2c1 1 2 2 3 3l2-1 2 2-2 2C4 10 0 6 0 2z" fill="#fff"/></svg>1800-417-2950</span>
    <span><svg width="8" height="6" viewBox="0 0 10 7"><rect width="10" height="7" fill="#fff"/><path d="M0 0l5 4 5-4" stroke="#f5b30c" fill="none"/></svg>hello@votrel-events.com</span>
  </div>
</div>

<header class="abs header">
  <div class="abs brand"><i></i>VoTrel</div>
  <div class="abs social"><span></span><span></span><span></span><span></span><span></span></div>
</header>

<nav class="abs nav">
  <a class="active" style="width:55px">Home</a>
  <a style="width:65px">About Us</a>
  <a style="width:70px">Courses <svg width="6" height="4" viewBox="0 0 6 4"><path d="M0 0l3 3 3-3" stroke="#333" fill="none"/></svg></a>
  <a style="width:55px">Events</a>
  <a style="width:55px">News</a>
  <a style="width:57px">Gallery</a>
  <a style="width:72px;border-right:0;color:#555">Contact Us</a>
  <a class="search"><svg width="9" height="9" viewBox="0 0 10 10"><circle cx="4" cy="4" r="3" stroke="#aaa" fill="none" stroke-width="1.3"/><path d="M6.3 6.3L9.5 9.5" stroke="#aaa" stroke-width="1.3"/></svg></a>
</nav>

<div class="abs slide-arrow left"><svg width="10" height="16" viewBox="0 0 10 16"><path d="M8 1L2 8l6 7" stroke="#f5b30c" stroke-width="1.5" fill="none"/></svg></div>
<div class="abs slide-arrow right"><svg width="10" height="16" viewBox="0 0 10 16"><path d="M2 1l6 7-6 7" stroke="#f5b30c" stroke-width="1.5" fill="none"/></svg></div>

<div class="abs hero-photo" role="img" aria-label="Photo of a smiling woman with long curly hair leaning on her arms"></div>
<h1 class="abs slogan pt">Curta sua festa desde já !</h1>
<h2 class="abs slogan en">Enjoy our party now !</h2>

<div class="abs features">
  <div class="feature f1"><div class="badge"><svg width="22" height="20" viewBox="0 0 22 20"><path d="M11 19L2 10a5 5 0 0 1 9-6 5 5 0 0 1 9 6z" fill="#e0a10a"/></svg></div>Link</div>
  <div class="feature f2"><div class="badge"><svg width="20" height="20" viewBox="0 0 20 20"><path d="M3 17l1-5L14 2l4 4L8 16z" fill="#d4950a"/></svg></div>Link</div>
  <div class="feature f3"><div class="badge"><svg width="22" height="22" viewBox="0 0 22 22"><path d="M11 1l3 7h7l-6 5 2 8-6-4-6 4 2-8-6-5h7z" fill="#eaab10"/></svg></div>Link</div>
  <div class="feature f4"><div class="badge"><svg width="22" height="20" viewBox="0 0 22 20"><path d="M11 1L1 10h3v9h5v-6h4v6h5v-9h3z" fill="#f5b30c"/></svg></div>Link</div>
  <div class="feature f5"><div class="badge"><svg width="18" height="14" viewBox="0 0 18 14"><rect width="18" height="14" rx="3" fill="#f5b30c"/><path d="M7 4l5 3-5 3z" fill="#fff"/></svg></div>Take a Tour</div>
</div>

<main class="abs content">
  <div class="abs col-rule" style="left:147px"></div>
  <div class="abs col-rule" style="left:387px"></div>

  <section class="abs" style="left:16px;top:13px;width:115px">
    <div class="block-title">R.S.V.P.»</div>
    <p class="copy" style="margin:10px 0 8px">Li Europan lingues es membres del sam familie.</p>
    <div class="field">Event ID<svg width="4" height="7" viewBox="0 0 4 7"><path d="M0 3l2-3 2 3zM0 4l2 3 2-3z" fill="#888"/></svg></div>
    <div class="field" style="margin-top:6px">Password</div>
    <div class="btn" style="width:38px;margin:6px 0 0 auto">Search</div>
  </section>
  <div class="abs hrule" style="left:0;top:159px;width:147px"></div>

  <section class="abs" style="left:16px;top:168px;width:115px">
    <div class="block-title">Log In.»</div>
    <p class="copy" style="margin:10px 0 8px">Li Europan lingues es membres del sam familie.</p>
    <div class="field">Email</div>
    <div class="field" style="margin-top:5px">Password</div>
    <div class="btn" style="width:38px;margin:6px 0 0 auto">Go</div>
  </section>
  <div class="abs hrule" style="left:0;top:306px;width:147px"></div>

  <section class="abs" style="left:16px;top:320px;width:115px">
    <div class="block-title dark">Newsletter »</div>
    <p class="copy" style="margin:10px 0 7px">Li Europan lingues es membres del sam familie.</p>
    <div class="field">Email Address</div>
    <div class="btn" style="width:48px;margin:5px 0 0 auto">Subscribe</div>
  </section>
  <div class="abs seal" style="left:16px;top:471px" role="img" aria-label="Kendro secure site seal"></div>

  <section class="abs" style="left:163px;top:13px;width:208px">
    <div class="block-title">News »<div class="pager"><span><svg width="4" height="5" viewBox="0 0 4 5"><path d="M3 0L0 2.5 3 5z" fill="#2e0a05"/></svg></span><span><svg width="4" height="5" viewBox="0 0 4 5"><path d="M1 0l3 2.5L1 5z" fill="#2e0a05"/></svg></span></div></div>
  </section>
  <article class="abs news-item" style="left:163px;top:44px;width:225px;display:flex;gap:11px"><div class="thumb"></div><div style="width:178px"><h4>To an English person, it will seem like simply</h4><div class="date">Feb 13th, 2014</div><p class="copy">A un Angleso it va semblar un simplificat Angles</p></div></article>
  <article class="abs news-item" style="left:163px;top:112px;width:225px;display:flex;gap:11px"><div class="thumb"></div><div style="width:178px"><h4>To an English person, it will seem like simply</h4><div class="date">Feb 13th, 2014</div><p class="copy">A un Angleso it va semblar un simplificat Angles</p></div></article>
  <article class="abs news-item" style="left:163px;top:180px;width:225px;display:flex;gap:11px"><div class="thumb"></div><div style="width:178px"><h4>To an English person, it will seem like simply</h4><div class="date">Feb 13th, 2014</div><p class="copy">A un Angleso it va semblar un simplificat Angles</p></div></article>
  <div class="abs hrule" style="left:147px;top:244px;width:240px"></div>

  <section class="abs" style="left:163px;top:262px;width:208px">
    <div class="block-title dark">Video Tour »<div class="pager"><span><svg width="4" height="5" viewBox="0 0 4 5"><path d="M3 0L0 2.5 3 5z" fill="#2e0a05"/></svg></span><span><svg width="4" height="5" viewBox="0 0 4 5"><path d="M1 0l3 2.5L1 5z" fill="#2e0a05"/></svg></span></div></div>
    <div class="video" style="height:130px;margin-top:13px" role="img" aria-label="Video tour player"></div>
    <p class="copy" style="margin-top:7px">It wasn't a dream. His room, a proper human room although a little too small</p>
  </section>

  <section class="abs" style="left:404px;top:14px;width:115px">
    <div class="block-title">Sponsors »<div class="pager"><span><svg width="4" height="5" viewBox="0 0 4 5"><path d="M3 0L0 2.5 3 5z" fill="#2e0a05"/></svg></span><span><svg width="4" height="5" viewBox="0 0 4 5"><path d="M1 0l3 2.5L1 5z" fill="#2e0a05"/></svg></span></div></div>
  </section>
  <div class="abs ad" style="left:419px;top:46px" aria-label="Paid ad space"></div>
  <div class="abs ad" style="left:419px;top:82px" aria-label="Paid ad space"></div>
  <div class="abs ad" style="left:419px;top:119px" aria-label="Paid ad space"></div>
  <div class="abs hrule" style="left:387px;top:173px;width:147px"></div>

  <section class="abs" style="left:404px;top:197px;width:115px">
    <div class="block-title">Save the Date »</div>
  </section>
  <div class="abs event" style="left:404px;top:229px;display:flex;gap:9px"><div class="cal"><b>FEB</b><span>08</span></div><div style="width:80px"><h4>The new common will be more&nbsp; simple</h4><p>9:00am to 1:00pm</p></div></div>
  <div class="abs event" style="left:404px;top:273px;display:flex;gap:9px"><div class="cal"><b>FEB</b><span>10</span></div><div style="width:80px"><h4>The new common will be more&nbsp; simple</h4><p>9:00am to 1:00pm</p></div></div>
  <div class="abs event" style="left:404px;top:318px;display:flex;gap:9px"><div class="cal"><b>FEB</b><span>14</span></div><div style="width:80px"><h4>The new common will be more&nbsp; simple</h4><p>9:00am to 1:00pm</p></div></div>
  <div class="abs hrule" style="left:387px;top:369px;width:147px"></div>
</main>

<footer class="abs footer">
  <h3 class="foot-title" style="left:177px">About Us</h3>
  <p class="abs foot-copy" style="left:177px;top:66px;width:116px">Quisque bibendum erat feugiat rhoncus tincidunt ipsum mi facilisis nisl, nec eleifend enim massa ac purus. Integer malesuada faucibus auctor vivamus accumsan justo.</p>

  <h3 class="foot-title" style="left:306px">Tag Cloud</h3>
  <div class="abs tags" style="left:306px;top:70px"><span>Education</span><span style="margin-left:2px;width:46px;justify-content:center">Funny</span><span>College</span><span>Parties</span><span>Art</span><span>Design</span><span>Music</span><span style="width:55px;justify-content:center">March</span></div>

  <h3 class="foot-title" style="left:436px">Twitter Feed</h3>
  <p class="abs tweet" style="left:436px;top:67px;width:110px"><b>@Mira</b> imperdiet adipiscing elit ac fermentum. nullam et<small>about 6 hours ago</small></p>
  <p class="abs tweet" style="left:436px;top:118px;width:110px"><b>@VoTrel</b> imperdiet adipiscing elit ac fermentum. nullam et<small>about 6 hours ago</small></p>

  <h3 class="foot-title" style="left:570px">Photo Gallery »</h3>
  <div class="abs gallery" style="left:564px;top:64px"><span></span><span></span><span></span><span></span><span></span><span></span></div>

  <div class="abs bottom-bar"><span>© Copyright&nbsp; <span style="color:#fff">VoTrel</span></span><span style="color:#fff">Top <svg width="6" height="4" viewBox="0 0 6 4"><path d="M0 4l3-3 3 3" stroke="#fff" fill="none"/></svg></span></div>
</footer>

</body>
</html>
```